We have a cheerleading competition on Sunday the 30 and I want to encourage parent assistance, support and participation!
Updates

1. Please add:
    Cheer Championship (instead of Cheerleading Competition)

2. Banner: Let's support our Cheerleaders!

Under Banner have the Date in big

Before the Location add:  Joins us at:

Thank you all for your designs and taking the time to submit them. I greatly appreciate them and they were all lovely. I could only pick one though! Hope to have you again on my next project.

Regards, Dariela

Requirements
Must have
• Flyer should be 1/2 of an A4 page. kid friendly. The cheerleaders are 6-13 yrs old.
The colors Burgundy, Gold (yellow) and White - It should have the team Eagle design on it. Bayview Ridge Otters

Simple design. It will contain an address, times and dates.

should have all of the following information:

Date: Sunday - October 30th 2011
Location: Harbor Crest Arena at the Coastal Pines College
3870 Pellman Lane
Coral gables, FL 33146
Time: Tickets on sale 8:30AM - Doors Open 9:00AM Starts: 10:00AM
Prices: Adults $10.00 Children $5.00 - Cash Only

```html
<!DOCTYPE html>
<html lang="en">
<head>
<meta charset="utf-8">
<title>Cheer Championship Flyer</title>
<link rel="stylesheet" href="https://fonts.googleapis.com/css2?family=Source+Sans+3:wght@400;600;700&display=swap">
<style>
  :root {
    --burgundy: #7c1624;
    --burgundy-deep: #6e1220;
    --body-red: #7a1a22;
    --label-orange: #b8461c;
    --gold: #f3c21a;
    --gold-orange: #e08a1e;
    --rule-grey: #8a8a8a;
    --paper: #ffffff;
    --faint: #ece7e2;
  }
  * { margin: 0; padding: 0; box-sizing: border-box; }
  html, body { width: 1200px; height: 849px; overflow: hidden; background: var(--paper); }
  body { font-family: "Source Sans 3", "Myriad Pro", Arial, sans-serif; color: var(--body-red); }
  .flyer { position: relative; width: 1200px; height: 849px; overflow: hidden; background: var(--paper); }

  .mascot-watermark {
    position: absolute; left: 0; top: 110px; width: 680px; height: 700px;
    background: radial-gradient(ellipse at 40% 45%, var(--faint) 0%, rgba(236,231,226,0.6) 45%, rgba(255,255,255,0) 72%);
  }
  .mascot-head {
    position: absolute; left: 30px; top: 12px; width: 304px; height: 230px;
    background: radial-gradient(ellipse at 45% 50%, var(--burgundy) 0%, #8f2230 55%, rgba(224,170,60,0.85) 100%);
    border-radius: 46% 54% 40% 60% / 55% 50% 50% 45%;
  }

  .title {
    position: absolute; left: 397px; top: 52px; font-size: 62px; line-height: 1;
    color: var(--burgundy); font-weight: 400; letter-spacing: 0.2px; white-space: nowrap;
  }
  .title strong { font-weight: 700; }
  .title-rule { position: absolute; left: 383px; top: 139px; width: 771px; height: 2px; background: var(--rule-grey); }

  .banner {
    position: absolute; left: 470px; top: 170px; font-size: 32px; font-weight: 700;
    color: var(--burgundy); white-space: nowrap;
  }
  .event-date {
    position: absolute; left: 416px; top: 228px; font-size: 50px; font-weight: 700;
    color: var(--burgundy); white-space: nowrap;
  }

  .join { position: absolute; left: 157px; top: 316px; font-size: 34px; font-weight: 700; color: var(--label-orange); }

  .detail { position: absolute; left: 90px; }
  .detail .bullet {
    position: absolute; left: 0; top: 4px; width: 58px; height: 30px;
    background: linear-gradient(90deg, var(--burgundy) 0%, var(--burgundy) 55%, var(--gold-orange) 100%);
    border-radius: 50% 40% 40% 50%;
  }
  .detail h2 { margin-left: 67px; font-size: 29px; font-weight: 700; color: var(--label-orange); line-height: 1.2; }
  .detail p { margin-left: 67px; font-size: 29px; font-weight: 400; color: var(--body-red); line-height: 41px; }
  .location { top: 370px; }
  .time { top: 557px; }

  .cheerleader {
    position: absolute;
    background: radial-gradient(ellipse at 50% 50%, var(--burgundy) 0%, rgba(124,22,36,0.85) 45%, rgba(124,22,36,0) 75%);
  }
  .cheerleader-small { left: 620px; top: 500px; width: 140px; height: 200px; }
  .cheerleader-large { left: 860px; top: 318px; width: 340px; height: 458px; }

  .gold-stripe {
    position: absolute; left: 0; top: 746px; width: 1200px; height: 30px;
    background: linear-gradient(90deg, var(--gold-orange) 0%, var(--gold) 45%, #fbe9a6 100%);
  }
  .price-band {
    position: absolute; left: 0; top: 776px; width: 1200px; height: 73px;
    background: var(--burgundy-deep); color: var(--paper);
    display: flex; align-items: center; justify-content: center;
    font-size: 29px; font-weight: 400;
  }
  .price-band strong { font-weight: 700; }
</style>
</head>
<body>
<main class="flyer">
  <div class="mascot-watermark" role="img" aria-label="Faint large team eagle mascot in the background"></div>
  <div class="mascot-head" role="img" aria-label="Team eagle mascot head, burgundy with gold beak"></div>

  <h1 class="title"><strong>Cheer</strong> Championship</h1>
  <div class="title-rule"></div>

  <p class="banner">Lets support our Cheerleaders!</p>
  <p class="event-date">Sunday - October 30th 2011</p>

  <p class="join">Joins us at:</p>

  <section class="detail location">
    <span class="bullet" role="img" aria-label="Small eagle mascot bullet"></span>
    <h2>Location:</h2>
    <p>Harbor Crest Arena at the Coastal Pines College<br>3870 Pellman Lane<br>Coral gables, FL 33146</p>
  </section>

  <section class="detail time">
    <span class="bullet" role="img" aria-label="Small eagle mascot bullet"></span>
    <h2>Time:</h2>
    <p>Tickets on sale 8:30AM<br>Doors Open 9:00AM<br>Starts: 10:00AM</p>
  </section>

  <div class="cheerleader cheerleader-small" role="img" aria-label="Burgundy silhouette of a jumping cheerleader with pom-poms"></div>
  <div class="cheerleader cheerleader-large" role="img" aria-label="Large burgundy silhouette of a cheerleader raising pom-poms"></div>

  <div class="gold-stripe"></div>
  <footer class="price-band"><span><strong>Prices:</strong>&nbsp;Adults $10.00 Children $5.00 - <strong>Cash Only</strong></span></footer>
</main>
</body>
</html>
```